Poster of Core Values & Motto

Create our core values poster and motto. Attached are our core values and our Motto. This poster represents both of our companies Tidy Pulp & CuraBinix.

Target Market(s)

Our team / employees

Industry/Entity Type

Shredding and Medical Waste

Colors
59FF00
82FF00
B8FF75
E3FFCB
F4FFEA
EB3D1F
EC4F4E
F09395
F8D3D4
FCEDEE

Requirements
Must have
• Include both companies logos

```html
<!DOCTYPE html>
<html lang="en">
<head>
<meta charset="utf-8">
<title>Core Values Poster — Tidy Pulp &amp; CuraBinix</title>
<link rel="stylesheet" href="https://fonts.googleapis.com/css2?family=Montserrat:wght@300;400;700;800;900&display=swap">
<style>
  :root {
    --navy: #0b1e30;
    --green: #00ab4e;
    --aqua: #1fcfbf;
    --teal-card: #00a69c;
    --tagline: #2ab6d6;
    --card-text: #d3f1ee;
    --white: #ffffff;
    --footer-grey: #cccccc;
    --brand-green: #00a651;
    --brand-red: #e0312a;
  }
  * { margin: 0; padding: 0; box-sizing: border-box; }
  html, body { width: 800px; height: 1200px; overflow: hidden; background: var(--navy); }
  .poster {
    position: relative; width: 800px; height: 1200px; overflow: hidden;
    background: var(--navy);
    font-family: "Montserrat", Arial, sans-serif;
  }
  .helix-art {
    position: absolute; left: 290px; top: 0; width: 510px; height: 800px;
    background:
      radial-gradient(ellipse 90px 260px at 230px 300px, rgba(60,230,220,0.55), rgba(40,150,220,0.15) 70%, transparent 100%),
      radial-gradient(ellipse 220px 380px at 260px 330px, rgba(30,110,200,0.35), transparent 75%),
      linear-gradient(160deg, rgba(20,80,160,0.0) 0%, rgba(20,90,170,0.25) 45%, rgba(20,80,160,0) 100%);
  }
  .motto-words { position: absolute; left: 70px; top: 156px; }
  .motto-word {
    display: block; height: 46px; margin-bottom: 7px;
    background: var(--green); color: var(--navy);
    font-weight: 900; font-size: 29px; line-height: 46px;
    padding-left: 14px; letter-spacing: 0.3px;
  }
  .motto-word.purpose { width: 200px; }
  .motto-word.cause { width: 152px; }
  .motto-word.passion { width: 188px; }
  .tagline {
    position: absolute; left: 70px; top: 337px;
    color: var(--tagline); font-weight: 300; font-size: 26px; line-height: 35px;
    letter-spacing: 0.6px;
  }
  .values-heading {
    position: absolute; left: 282px; top: 484px; width: 236px; height: 46px;
    background: var(--aqua); color: var(--navy);
    font-weight: 900; font-size: 22px; line-height: 46px; text-align: center;
  }
  .values-grid {
    position: absolute; left: 70px; top: 561px;
    display: grid; grid-template-columns: repeat(3, 211px); grid-auto-rows: 211px;
    gap: 13px;
  }
  .value-card {
    background: var(--teal-card); text-align: center; color: var(--white);
    padding-top: 36px;
  }
  .value-icon { width: 42px; height: 42px; display: block; margin: 0 auto; }
  .value-title {
    margin-top: 30px; font-weight: 800; font-size: 12.5px; letter-spacing: 0.1px;
  }
  .value-rule { width: 20px; height: 2px; background: var(--navy); margin: 8px auto 12px; }
  .value-text {
    color: var(--card-text); font-weight: 400; font-size: 11.5px; line-height: 15px;
    padding: 0 20px;
  }
  .partner-band {
    position: absolute; left: 70px; top: 1046px; width: 660px; height: 105px;
    background: var(--footer-grey);
    display: flex; align-items: center; justify-content: center; gap: 70px;
  }
  .partner { display: flex; align-items: center; gap: 10px; font-weight: 700; font-size: 24px; }
  .partner-dot { width: 22px; height: 22px; border-radius: 50%; }
  .partner.tidy { color: var(--brand-green); }
  .partner.tidy .partner-dot { background: var(--brand-green); }
  .partner.cura { color: var(--brand-red); }
</style>
</head>
<body>
<main class="poster">
  <div class="helix-art" role="img" aria-label="Glowing blue and teal DNA double helix made of dots"></div>

  <div class="motto-words">
    <span class="motto-word purpose">PURPOSE</span>
    <span class="motto-word cause">CAUSE</span>
    <span class="motto-word passion">PASSION</span>
  </div>

  <p class="tagline">Remind people<br>what great service<br>looks like</p>

  <h2 class="values-heading">CORE VALUES</h2>

  <section class="values-grid">
    <article class="value-card">
      <svg class="value-icon" viewBox="0 0 60 42" fill="none" stroke="#0b1e30" stroke-width="2.4" stroke-linecap="round" stroke-linejoin="round" style="width:62px">
        <circle cx="9" cy="7" r="6"/><circle cx="30" cy="7" r="6"/><circle cx="51" cy="7" r="6"/>
        <path d="M2 34V22q0-5 6-5 4 0 7 4l4 5"/><path d="M58 34V22q0-5-6-5-4 0-7 4l-4 5"/>
        <path d="M19 26q3-9 11-9t11 9"/><path d="M12 30h36"/><path d="M16 30v5M44 30v5"/>
      </svg>
      <h3 class="value-title">SYNERGY / TEAMWORK</h3>
      <div class="value-rule"></div>
      <p class="value-text">Remind people what great service looks like</p>
    </article>
    <article class="value-card">
      <svg class="value-icon" viewBox="0 0 40 42" fill="none" stroke="#0b1e30" stroke-width="2.4" stroke-linejoin="round">
        <path d="M20 2l4 3 5-1 2 4 4 3-1 5 1 4-4 3-2 4-5-1-4 3-4-3-5 1-2-4-4-3 1-4-1-5 4-3 2-4 5 1z"/>
        <circle cx="20" cy="15" r="6"/>
        <path d="M12 27l-5 12 6-3 3 5 4-10M28 27l5 12-6-3-3 5-4-10"/>
      </svg>
      <h3 class="value-title">EXCELLENCE</h3>
      <div class="value-rule"></div>
      <p class="value-text">Exceed expectations with a smile</p>
    </article>
    <article class="value-card">
      <svg class="value-icon" viewBox="0 0 44 42" fill="none" stroke="#0b1e30" stroke-width="2.4" stroke-linecap="round" stroke-linejoin="round">
        <path d="M6 17A16 16 0 0 1 36 12"/><path d="M38 25A16 16 0 0 1 8 30"/>
        <path d="M2 21l4-4 4 4M34 21l4 4 4-4"/>
        <circle cx="22" cy="21" r="4" fill="#0b1e30"/>
        <path d="M22 12v3M22 27v3M13 21h3M28 21h3M16 15l2 2M26 25l2 2M28 15l-2 2M16 27l2-2"/>
      </svg>
      <h3 class="value-title">SYNERGY / TEAMWORK</h3>
      <div class="value-rule"></div>
      <p class="value-text">On-Time, Sense of urgency, always trying to improve</p>
    </article>
    <article class="value-card">
      <svg class="value-icon" viewBox="0 0 40 42" fill="none" stroke="#0b1e30" stroke-width="2.6" stroke-linecap="round" stroke-linejoin="round">
        <path d="M20 2l16 6v12q0 13-16 20Q4 33 4 20V8z"/>
        <path d="M13 21l5 5 9-9"/>
      </svg>
      <h3 class="value-title">SYNERGY / TEAMWORK</h3>
      <div class="value-rule"></div>
      <p class="value-text">We are just as secure as an armored truck with money</p>
    </article>
    <article class="value-card">
      <svg class="value-icon" viewBox="0 0 42 42" fill="none" stroke="#0b1e30" stroke-width="2.6" stroke-linecap="round" stroke-linejoin="round">
        <path d="M13 3h16l10 10v16L29 39H13L3 29V13z"/>
        <path d="M14 21l5 5 9-9"/>
      </svg>
      <h3 class="value-title">SYNERGY / TEAMWORK</h3>
      <div class="value-rule"></div>
      <p class="value-text">Do the right thing</p>
    </article>
    <article class="value-card">
      <svg class="value-icon" viewBox="0 0 42 42" fill="none" stroke="#0b1e30" stroke-width="2.4" stroke-linecap="round" stroke-linejoin="round">
        <rect x="2" y="18" width="8" height="20"/>
        <path d="M10 20l8-9 2-9q5 0 5 6l-1 9h12q3 0 3 3t-3 3q3 0 3 3t-3 3q2 0 2 3t-3 3q2 0 2 2.5T34 38H10"/>
      </svg>
      <h3 class="value-title">SYNERGY / TEAMWORK</h3>
      <div class="value-rule"></div>
      <p class="value-text">Do what you say you will do</p>
    </article>
  </section>

  <footer class="partner-band">
    <div class="partner tidy"><span class="partner-dot"></span>Tidy Pulp</div>
    <div class="partner cura">CuraBinix</div>
  </footer>
</main>
</body>
</html>
```